2 x storefront vinyl request

We are transitioning to a storefront office and need two vinyls for the windows.

First vinyl: Use the Dalton Rivers logo, website (www.daltonriversholdings.example) and leasing office number ((555) 318-4472)

Second vinyl: Maintenance Division & phone number (555) 318-4472

```html
<!DOCTYPE html>
<html lang="en">
<head>
<meta charset="utf-8">
<title>Dalton Rivers Properties – Storefront Vinyls</title>
<link rel="stylesheet" href="https://fonts.googleapis.com/css2?family=Open+Sans:wght@600;700&display=swap">
<style>
  :root {
    --page: #ffffff;
    --blue-light: #3f93d6;
    --blue-mid: #2c7cc6;
    --blue-deep: #1f64ad;
    --ink: #111111;
    --white: #ffffff;
    --yellow: #fcd10f;
    --red: #e8202a;
    --glass-1: #7fb3bd;
    --glass-2: #3c5d7a;
    --glass-3: #1c2638;
    --wood-1: #8a5a3a;
    --wood-2: #5e3a24;
    --wood-3: #3c2517;
  }
  * { box-sizing: border-box; margin: 0; padding: 0; }
  html, body {
    width: 1200px;
    height: 1200px;
    overflow: hidden;
    background: var(--page);
    font-family: "Open Sans", Arial, sans-serif;
  }
  .canvas {
    width: 1200px;
    height: 1200px;
    display: flex;
    align-items: center;
    justify-content: center;
    gap: 20px;
  }
  .vinyl {
    width: 570px;
    height: 570px;
    display: flex;
  }
  .vinyl__info {
    position: relative;
    width: 286px;
    height: 100%;
    background: radial-gradient(ellipse at 50% 45%, var(--blue-light) 0%, var(--blue-mid) 55%, var(--blue-deep) 100%);
    color: var(--white);
    text-align: center;
    overflow: hidden;
  }
  .vinyl__photo {
    width: 284px;
    height: 100%;
  }
  .vinyl__photo--tower {
    background: linear-gradient(100deg, var(--glass-2) 0%, var(--glass-1) 30%, var(--glass-3) 48%, var(--glass-2) 62%, var(--glass-1) 85%, var(--glass-2) 100%);
  }
  .vinyl__photo--tools {
    background: linear-gradient(135deg, var(--wood-1) 0%, var(--wood-2) 55%, var(--wood-3) 100%);
  }
  .brand-name {
    position: absolute;
    top: 118px;
    left: 0;
    width: 100%;
    font-weight: 700;
    font-size: 27px;
    line-height: 1.05;
    color: var(--ink);
    letter-spacing: 0.5px;
    text-transform: uppercase;
  }
  .contact {
    position: absolute;
    left: 0;
    width: 100%;
    font-weight: 700;
  }
  .contact__label { font-size: 30px; line-height: 1.15; }
  .contact__phone { font-size: 24px; font-weight: 600; line-height: 1.2; }
  .contact__web { font-size: 19px; line-height: 1.25; margin-top: 32px; }
  .division { font-size: 30px; line-height: 1.2; }
  .chevron {
    position: absolute;
    left: 0;
    bottom: 0;
    width: 286px;
    height: 570px;
  }
</style>
</head>
<body>
<main class="canvas">

  <section class="vinyl vinyl--office">
    <div class="vinyl__info">
      <p class="brand-name">Dalton<br>Rivers<br>Properties</p>
      <div class="contact" style="top: 312px;">
        <p class="contact__label">office number</p>
        <p class="contact__phone">(555) 318-4472</p>
        <p class="contact__web">www.daltonrivers<br>holdings.example</p>
      </div>
      <svg class="chevron" viewBox="0 0 286 570" aria-hidden="true">
        <polygon points="0,519 146,566 286,519 286,570 0,570" fill="var(--yellow)"/>
        <polygon points="0,531 146,572 286,531 286,570 0,570" fill="var(--red)"/>
      </svg>
    </div>
    <div class="vinyl__photo vinyl__photo--tower" role="img" aria-label="Photo looking up at a glass office tower against a cloudy sky"></div>
  </section>

  <section class="vinyl vinyl--maintenance">
    <div class="vinyl__info">
      <p class="brand-name">Dalton<br>Rivers<br>Properties</p>
      <div class="contact" style="top: 318px;">
        <p class="division">Maintenance<br>Division</p>
        <p class="contact__label" style="margin-top: 12px;">phone number</p>
        <p class="contact__phone">(555) 318-4472</p>
      </div>
      <svg class="chevron" viewBox="0 0 286 570" aria-hidden="true">
        <polygon points="0,519 146,566 286,519 286,570 0,570" fill="var(--yellow)"/>
        <polygon points="0,531 146,572 286,531 286,570 0,570" fill="var(--red)"/>
      </svg>
    </div>
    <div class="vinyl__photo vinyl__photo--tools" role="img" aria-label="Photo of hand tools – hammer, pliers, hex keys, wrenches and a utility knife – laid out on a wooden surface"></div>
  </section>

</main>
</body>
</html>
```